Creative Brief
Investment Banking Company Stationary
Business card, Letterhead, Envelope, Fax Cover
Professional
Daniyar Ospanturov
Managing Partner
27B Zheltoksan St,
Almaty, 050118
Kazakhstan
dospanturov@mailvero.kz
www.veltrafin.kz
The name of the company is Veltra Finance, LLP. In addition to the logo there should be text that includes the official name of the company.
I will need business cards for 3 other employees as well. Please message me for their relevant info.
Logo or blank

```html
<!DOCTYPE html>
<html lang="en">
<head>
<meta charset="utf-8">
<title>Veltra Finance – Stationery Set</title>
<link rel="stylesheet" href="https://fonts.googleapis.com/css2?family=Arimo:wght@400;700&display=swap">
<style>
  :root{
    --backdrop:#8c8c8c;
    --paper:#ffffff;
    --navy:#0c2f63;
    --blue-deep:#0a2b5c;
    --blue-mid:#1c55a0;
    --blue-light:#3f7cc8;
    --ink:#333a44;
    --rule:#9aa3ad;
    --ghost:#e6e9ed;
    --edge:#111318;
  }
  *{box-sizing:border-box;margin:0;padding:0}
  html,body{width:1200px;height:494px;overflow:hidden;background:var(--backdrop)}
  .canvas{position:relative;width:1200px;height:494px;font-family:"Arimo",Arial,sans-serif;color:var(--ink)}
  .sheet{position:absolute;background:var(--paper);overflow:hidden;box-shadow:0 2px 6px rgba(0,0,0,.35)}
  .sheet svg.sweep{position:absolute;inset:0;width:100%;height:100%}

  .brand{position:absolute;display:flex;align-items:center;gap:4px}
  .brand-square{width:6px;height:6px;background:var(--navy)}
  .brand-name{font-weight:700;color:var(--navy);font-size:9px;white-space:nowrap}

  .ghost-name{position:absolute;font-weight:700;color:var(--ghost);font-size:26px;white-space:nowrap}

  .tiny{font-size:5px;line-height:7px;color:var(--ink);white-space:nowrap}
  .contact-top{position:absolute;top:20px;right:40px}
  .footer{position:absolute;left:20px;bottom:22px}

  /* letterhead */
  .letterhead{left:127px;top:19px;width:281px;height:454px}
  .letterhead .brand{left:14px;top:20px}
  .letterhead .ghost-name{left:14px;top:220px}

  /* fax cover */
  .fax{left:420px;top:19px;width:283px;height:454px}
  .fax .brand{left:14px;top:20px}
  .fax-fields{position:absolute;left:14px;top:160px;width:230px;display:grid;grid-template-columns:1fr 1fr;column-gap:14px;row-gap:7px}
  .field{display:flex;align-items:flex-end;gap:4px;font-size:6px}
  .field .label{width:20px}
  .field .line{flex:1;border-bottom:.6px solid var(--rule);height:6px}
  .fax-checks{position:absolute;left:14px;top:226px;display:flex;gap:10px;font-size:6px}
  .check{display:flex;align-items:center;gap:2px}
  .check .box{width:5px;height:5px;border:.6px solid var(--ink)}

  /* business card */
  .card{left:24px;top:357px;width:96px;height:86px}
  .card .brand{left:7px;top:36px;gap:3px}
  .card .brand-name{font-size:5.5px}
  .card .brand-square{width:4px;height:4px}
  .card-person{position:absolute;left:7px;top:8px}
  .card-person .tiny{font-size:3.2px;line-height:4.4px}

  /* envelope */
  .envelope{position:absolute;left:739px;top:228px;width:440px;height:246px}
  .envelope-flap{position:absolute;left:0;top:0;width:440px;height:56px}
  .flap-name{position:absolute;left:0;right:0;top:14px;text-align:center;transform:rotate(180deg);font-weight:700;font-size:10px;color:var(--navy)}
  .envelope-body{left:0;top:54px;width:440px;height:192px}
  .envelope-body .brand{left:34px;top:64px;gap:5px}
  .envelope-body .brand-name{font-size:12px}
  .envelope-body .brand-square{width:8px;height:8px}
  .envelope-body .footer{left:32px;bottom:16px}
</style>
</head>
<body>
<main class="canvas">

  <section class="sheet card" aria-label="Business card">
    <svg class="sweep" viewBox="0 0 96 86" preserveAspectRatio="none">
      <defs>
        <linearGradient id="cardBlue" x1="0" y1="0" x2="1" y2="0">
          <stop offset="0" stop-color="var(--blue-deep)"/><stop offset=".6" stop-color="var(--blue-mid)"/><stop offset="1" stop-color="var(--blue-light)"/>
        </linearGradient>
      </defs>
      <path d="M96 6 C70 30 66 60 52 86 L96 86 Z" fill="url(#cardBlue)"/>
      <path d="M96 4 C68 30 64 60 49 86" fill="none" stroke="var(--edge)" stroke-width="1.2"/>
    </svg>
    <div class="card-person">
      <p class="tiny"><b>Daniyar Ospanturov</b></p>
      <p class="tiny">Managing Partner</p>
      <p class="tiny">dospanturov@mailvero.kz</p>
    </div>
    <div class="brand"><span class="brand-square"></span><span class="brand-name">Veltra Finance</span></div>
  </section>

  <section class="sheet letterhead" aria-label="Letterhead">
    <svg class="sweep" viewBox="0 0 281 454" preserveAspectRatio="none">
      <defs>
        <linearGradient id="lhBlue" x1="0" y1="0" x2="1" y2="0">
          <stop offset="0" stop-color="var(--blue-deep)"/><stop offset=".5" stop-color="var(--blue-mid)"/><stop offset="1" stop-color="var(--blue-light)"/>
        </linearGradient>
      </defs>
      <path d="M281 40 C240 130 236 320 170 454 L281 454 Z" fill="url(#lhBlue)"/>
      <path d="M281 34 C236 130 230 320 160 454" fill="none" stroke="var(--edge)" stroke-width="3"/>
    </svg>
    <div class="brand"><span class="brand-square"></span><span class="brand-name">Veltra Finance</span></div>
    <div class="contact-top">
      <p class="tiny">dospanturov@mailvero.kz</p>
      <p class="tiny">www.veltrafin.kz</p>
    </div>
    <p class="ghost-name" aria-hidden="true">Veltra Finance</p>
    <div class="footer">
      <p class="tiny">27B Zheltoksan St, Almaty, 050118 Kazakhstan</p>
      <p class="tiny">Tel +7 (000) 555 0142 · Fax +7 (000) 555 0143</p>
    </div>
  </section>

  <section class="sheet fax" aria-label="Fax cover sheet">
    <svg class="sweep" viewBox="0 0 283 454" preserveAspectRatio="none">
      <defs>
        <linearGradient id="faxBlue" x1="0" y1="0" x2="1" y2="0">
          <stop offset="0" stop-color="var(--blue-deep)"/><stop offset=".5" stop-color="var(--blue-mid)"/><stop offset="1" stop-color="var(--blue-light)"/>
        </linearGradient>
      </defs>
      <path d="M283 40 C242 130 238 320 172 454 L283 454 Z" fill="url(#faxBlue)"/>
      <path d="M283 34 C238 130 232 320 162 454" fill="none" stroke="var(--edge)" stroke-width="3"/>
    </svg>
    <div class="brand"><span class="brand-square"></span><span class="brand-name">Veltra Finance</span></div>
    <div class="contact-top">
      <p class="tiny">dospanturov@mailvero.kz</p>
      <p class="tiny">www.veltrafin.kz</p>
    </div>
    <div class="fax-fields">
      <div class="field"><span class="label">To</span><span class="line"></span></div>
      <div class="field"><span class="label">From</span><span class="line"></span></div>
      <div class="field"><span class="label">Fax</span><span class="line"></span></div>
      <div class="field"><span class="label">Pages</span><span class="line"></span></div>
      <div class="field"><span class="label">Phone</span><span class="line"></span></div>
      <div class="field"><span class="label">Date</span><span class="line"></span></div>
      <div class="field"><span class="label">Re</span><span class="line"></span></div>
      <div class="field"><span class="label">CC</span><span class="line"></span></div>
    </div>
    <div class="fax-checks">
      <span class="check"><span class="box"></span>Urgent</span>
      <span class="check"><span class="box"></span>Please Reply</span>
    </div>
    <div class="footer">
      <p class="tiny">27B Zheltoksan St, Almaty, 050118 Kazakhstan</p>
      <p class="tiny">Tel +7 (000) 555 0142 · Fax +7 (000) 555 0143</p>
    </div>
  </section>

  <section class="envelope" aria-label="Envelope">
    <svg class="envelope-flap" viewBox="0 0 440 56" preserveAspectRatio="none">
      <defs>
        <linearGradient id="flapBlue" x1="0" y1="0" x2="1" y2="0">
          <stop offset="0" stop-color="var(--blue-deep)"/><stop offset=".5" stop-color="var(--blue-mid)"/><stop offset="1" stop-color="var(--blue-light)"/>
        </linearGradient>
      </defs>
      <path d="M0 56 L40 8 Q44 2 52 2 L388 2 Q396 2 400 8 L440 56 Z" fill="url(#flapBlue)"/>
      <path d="M30 56 L62 18 Q66 14 74 14 L366 14 Q374 14 378 18 L410 56 Z" fill="var(--paper)"/>
    </svg>
    <div class="envelope-flap"><p class="flap-name">Veltra Finance</p></div>
    <div class="sheet envelope-body">
      <svg class="sweep" viewBox="0 0 440 192" preserveAspectRatio="none">
        <defs>
          <linearGradient id="envBlue" x1="0" y1="0" x2="1" y2="0">
            <stop offset="0" stop-color="var(--blue-deep)"/><stop offset=".5" stop-color="var(--blue-mid)"/><stop offset="1" stop-color="var(--blue-light)"/>
          </linearGradient>
        </defs>
        <path d="M440 0 L360 0 C330 60 320 130 300 192 L440 192 Z" fill="url(#envBlue)"/>
        <path d="M352 0 C322 60 312 130 292 192" fill="none" stroke="var(--edge)" stroke-width="3"/>
      </svg>
      <div class="brand"><span class="brand-square"></span><span class="brand-name">Veltra Finance</span></div>
      <div class="footer">
        <p class="tiny">27B Zheltoksan St, Almaty, 050118 Kazakhstan</p>
        <p class="tiny">Tel +7 (000) 555 0142 · Fax +7 (000) 555 0143 · www.veltrafin.kz</p>
      </div>
    </div>
  </section>

</main>
</body>
</html>
```